I need a business card representing my company, VELDRA, it's an artist management and design company. Complete name is "VELDRA Artist Mgmt. + Design Co." I need it to be world class and very appealing, sophisticated and artistically unique.
Updates

Posted an updated Brief please see. I need a business card representing my company, VELDRA, it's an artist management and design company. Complete name is "VELDRA Artist Mgmt. + Design Co." I need it to be world class and very appealing, sophisticated and artistically unique.

Designs look the same

Designs look the same

Target Market(s)

Advertisers, Entertainment Companies, Commercial companies

Industry/Entity Type

Advertising

Contact Information for Business Card

I need a business card representing my company, VELDRA, it's an artist management and design company. Complete name is "VELDRA Artist Mgmt. + Design Co." I need it to be world class and very appealing, sophisticated and artistically unique. One side can be VELDRA Artist Mgmt. + Design Co. and the other my name, Teodoro Lindqvist, my contact telephone: 412.638.2957, email veldraartist@plumora.net, my address: 3264 Harwell Ave. #517 Miami, FL 33184

Font styles to use
Other font styles liked:
• Calibri

Colors
ffffff
0455a3
f37122

Requirements
Must have
• "VELDRA" stand out bigger than the rest of the text.
Nice to have
• Name "VELDRA" can be centered on one side or in the corner or along side edges, just need something cool and different.
Should not have
• I am open just try to keep it clean looking

```html
<!DOCTYPE html>
<html lang="en">
<head>
<meta charset="utf-8">
<title>VELDRA Business Card</title>
<link href="https://fonts.googleapis.com/css2?family=Roboto+Condensed:ital,wght@0,400;0,700;1,400&family=Roboto:wght@900&display=swap" rel="stylesheet">
<style>
  :root {
    --bg: #d6d6d6;
    --blue: #0455a3;
    --blue-deep: #063a78;
    --blue-band: #0a3f86;
    --white: #ffffff;
    --ink: #2b2b2b;
  }
  * { margin: 0; padding: 0; box-sizing: border-box; }
  html, body { width: 1200px; height: 1051px; overflow: hidden; }
  body {
    background: var(--bg);
    font-family: "Roboto Condensed", "Arial Narrow", sans-serif;
    position: relative;
  }
  .card {
    position: absolute;
    top: 381px;
    width: 520px;
    height: 289px;
    box-shadow: 14px 18px 28px rgba(0,0,0,0.28);
  }
  .card--front {
    left: 50px;
    background: radial-gradient(ellipse at 30% 45%, #0b56a8 0%, var(--blue) 25%, var(--blue-deep) 85%);
  }
  .card--back { left: 630px; background: var(--white); }

  .wordmark {
    font-family: "Roboto", sans-serif;
    font-weight: 900;
    letter-spacing: 1px;
    line-height: 1;
  }
  .front-brand {
    position: absolute;
    left: 0; right: 0; top: 112px;
    text-align: center;
    color: var(--white);
  }
  .front-brand .wordmark { font-size: 50px; }
  .tagline {
    margin-top: 6px;
    font-style: italic;
    font-size: 13.5px;
    letter-spacing: 2.2px;
    text-transform: uppercase;
  }

  .back-brand {
    position: absolute;
    left: 0; right: 0; top: 56px;
    text-align: center;
    color: var(--blue);
  }
  .back-brand .wordmark { font-size: 44px; }

  .name-band {
    position: absolute;
    left: 0; top: 142px;
    width: 257px; height: 64px;
    background: var(--blue-band);
    color: var(--white);
    text-align: right;
    padding: 14px 14px 0 0;
  }
  .name-band .name { font-weight: 700; font-size: 19px; text-transform: uppercase; line-height: 1; }
  .name-band .role { font-weight: 700; font-size: 13px; line-height: 1.3; }

  .contacts {
    position: absolute;
    left: 296px; top: 142px;
    list-style: none;
    color: var(--ink);
    font-size: 13.5px;
    line-height: 17px;
  }
  .contacts li { display: flex; align-items: flex-start; margin-bottom: 7px; }
  .contacts svg { width: 15px; height: 15px; flex: none; margin: 1px 17px 0 0; fill: var(--ink); }
</style>
</head>
<body>
  <section class="card card--front">
    <div class="front-brand">
      <div class="wordmark">VELDRA</div>
      <div class="tagline">Artist Mgmt. + Design Co.</div>
    </div>
  </section>

  <section class="card card--back">
    <div class="back-brand"><div class="wordmark">VELDRA</div></div>
    <div class="name-band">
      <div class="name">Teodoro Lindqvist</div>
      <div class="role">founder/ceo</div>
    </div>
    <ul class="contacts">
      <li>
        <svg viewBox="0 0 24 24" aria-hidden="true"><path d="M6.6 10.8a15.1 15.1 0 0 0 6.6 6.6l2.2-2.2c.3-.3.7-.4 1-.2 1.1.4 2.3.6 3.6.6.6 0 1 .4 1 1V20c0 .6-.4 1-1 1C10.6 21 3 13.4 3 4c0-.6.4-1 1-1h3.5c.6 0 1 .4 1 1 0 1.3.2 2.5.6 3.6.1.3 0 .7-.2 1z"/></svg>
        <span>412.638.2957</span>
      </li>
      <li>
        <svg viewBox="0 0 24 24" aria-hidden="true"><path d="M2 5h20v2l-10 6L2 7z"/><path d="M2 9l10 6 10-6v10H2z"/></svg>
        <span>veldraartist@plumora.net</span>
      </li>
      <li>
        <svg viewBox="0 0 24 24" aria-hidden="true"><path d="M12 2a7 7 0 0 0-7 7c0 5.2 7 13 7 13s7-7.8 7-13a7 7 0 0 0-7-7zm0 9.5A2.5 2.5 0 1 1 12 6.5a2.5 2.5 0 0 1 0 5z"/></svg>
        <span>3264 Harwell<br>Ave. #517 Miami<br>FL 33184</span>
      </li>
    </ul>
  </section>
</body>
</html>
```